Luxury and organic beauty products need a Design

We need a bottle and packaging design for a new business in New Zealand, called Kelvara Botanicals. We are creating a selection of Luxury and premium products to have at the Kelvara luxury villa's (www.kelvaraluxuryvilla.com), as well to sell online and at boutique stores.

The products are: Body wash, Shampoo, Conditioner, Hand wash, Body lotion, Air fresheners and Bath salts.

We would like to use the Kelvara Botanicals logo in Silver as Kelvara Luxury Villa's a having it in Gold, so it separates the two products. Also the packaging will be Navy Blue along with the silver.

The final design should be sleek, sophisticated and have a luxury feel. Our customers will have the product in the bathroom and kitchen so the bottles must be proud to show off. " This should look and feel like a very high end product.

Boxes will have embossed writing (logo) and a slightly textured feel or look.

Please find attached images of some examples to use for inspiration only.

Target Market(s)

Luxury boutique villas, Boutique stores, High end stores

Industry/Entity Type

Personal and hair care

Colors
0054AA
0677BA
7BADD7
CADEEF
E8F1F8
FFC000
F8CF3A
FAE287
FDF2CF
FEFAEE

Requirements
Must have
• Use the provided Logo, look and feel luxurious, but at the same time organic
Nice to have
• A bottle that reminds precious stones. I have just attached an example
Should not have
• Dark colour, heavy fonts

```html
<!DOCTYPE html>
<html lang="en">
<head>
<meta charset="utf-8">
<title>Kelvara Botanicals – Packaging Labels</title>
<link rel="stylesheet" href="https://fonts.googleapis.com/css2?family=Jost:wght@300;400&family=Courgette&display=swap">
<style>
  :root {
    --backdrop: #efede8;
    --navy: #0b2a55;
    --navy-panel: #0d2f5e;
    --blue: #0054aa;
    --blue-mid: #0677ba;
    --blue-soft: #7badd7;
    --silver: #d3d7da;
    --silver-light: #eef1f3;
    --silver-dim: #9aa3aa;
  }
  * { margin: 0; padding: 0; box-sizing: border-box; }
  html, body {
    width: 1200px;
    height: 960px;
    overflow: hidden;
    background: var(--backdrop);
  }
  .canvas {
    position: relative;
    width: 1200px;
    height: 960px;
  }
  .label {
    position: absolute;
    background: var(--navy);
    overflow: hidden;
  }
  .label--shampoo { left: 152px; top: 218px; width: 285px; height: 577px; }
  .label--conditioner { left: 468px; top: 218px; width: 285px; height: 577px; }
  .label--bath-salt { left: 782px; top: 467px; width: 284px; height: 328px; }

  .label__pattern {
    position: absolute;
    inset: 0;
    background:
      radial-gradient(ellipse at 30% 18%, rgba(6,119,186,0.75), transparent 45%),
      radial-gradient(ellipse at 78% 55%, rgba(0,84,170,0.7), transparent 42%),
      radial-gradient(ellipse at 30% 85%, rgba(6,119,186,0.65), transparent 45%),
      radial-gradient(ellipse at 85% 10%, rgba(123,173,215,0.35), transparent 35%),
      linear-gradient(160deg, var(--blue), var(--navy) 55%, var(--blue));
  }

  .label__panel {
    position: absolute;
    background: var(--navy-panel);
    border: 2px solid var(--silver-dim);
    outline: 1px solid rgba(238,241,243,0.35);
    outline-offset: -5px;
    display: flex;
    flex-direction: column;
    align-items: center;
    color: var(--silver);
  }
  .label--shampoo .label__panel,
  .label--conditioner .label__panel {
    left: 50px; top: 129px; width: 183px; height: 206px;
    padding-top: 20px;
  }
  .label--bath-salt .label__panel {
    left: 41px; top: 56px; width: 202px; height: 193px;
    padding-top: 24px;
  }

  .brand__mark {
    width: 44px;
    height: 44px;
    border-radius: 50%;
    border: 2px solid var(--silver);
    margin-bottom: 14px;
  }
  .label--bath-salt .brand__mark { width: 42px; height: 42px; margin-bottom: 28px; }
  .brand__name {
    font-family: "Jost", sans-serif;
    font-weight: 300;
    color: var(--silver);
    text-align: center;
  }
  .brand__name-main {
    display: block;
    font-size: 21px;
    line-height: 1;
    letter-spacing: 0.04em;
    text-transform: uppercase;
  }
  .brand__name-sub {
    display: block;
    margin-top: 4px;
    font-size: 7px;
    line-height: 1;
    letter-spacing: 0.2em;
    text-transform: uppercase;
  }

  .product__name {
    font-family: "Courgette", cursive;
    font-weight: 400;
    color: var(--silver-light);
    line-height: 1;
  }
  .label--shampoo .product__name,
  .label--conditioner .product__name { font-size: 25px; margin-top: 18px; }
  .label--bath-salt .product__name { font-size: 18px; margin-top: 22px; }

  .product__volume {
    font-family: "Jost", sans-serif;
    font-weight: 400;
    font-size: 7.5px;
    line-height: 1;
    letter-spacing: 0.16em;
    color: var(--silver);
    margin-top: 16px;
    text-transform: uppercase;
  }
  .label--bath-salt .product__volume { margin-top: 8px; }
</style>
</head>
<body>
<main class="canvas">

  <section class="label label--shampoo">
    <div class="label__pattern" role="img" aria-label="Ginkgo leaf and flower pattern in blue tones with silver line art"></div>
    <div class="label__panel">
      <div class="brand__mark"></div>
      <p class="brand__name"><span class="brand__name-main">Kelvara</span><span class="brand__name-sub">Botanicals</span></p>
      <h2 class="product__name">Shampoo</h2>
      <p class="product__volume">100 ml</p>
    </div>
  </section>

  <section class="label label--conditioner">
    <div class="label__pattern" role="img" aria-label="Ginkgo leaf and flower pattern in blue tones with silver line art"></div>
    <div class="label__panel">
      <div class="brand__mark"></div>
      <p class="brand__name"><span class="brand__name-main">Kelvara</span><span class="brand__name-sub">Botanicals</span></p>
      <h2 class="product__name">Conditioner</h2>
      <p class="product__volume">100 ml</p>
    </div>
  </section>

  <section class="label label--bath-salt">
    <div class="label__pattern" role="img" aria-label="Ginkgo leaf and flower pattern in blue tones with silver line art"></div>
    <div class="label__panel">
      <div class="brand__mark"></div>
      <p class="brand__name"><span class="brand__name-main">Kelvara</span><span class="brand__name-sub">Botanicals</span></p>
      <h2 class="product__name">Bath Salt</h2>
      <p class="product__volume">150 grams</p>
    </div>
  </section>

</main>
</body>
</html>
```